family chiropractic health care team needs a modern business card design

Healthcare office with Chiropractors, Physiotherapists, Massage therapists and possibly other practitioners in the future. This is a friendly family office with patients of all ages (and lots of kids) that just moved into a new larger modern office.
Look at the website for photos of the office.
Design for the front and back of a business card required.
Text for the front:
Office logo and name of the office:
Bright Path Wellness Centre
Name of current Practitioner:
Dr. Marten Quovel B.Sc., D.C. Chiropractor
(But please include options to swap out name and title for other practitioners )

address:
218 Farrow Gate
Etobicoke ON.
K2J 6P4
Phone: 416-872-0196 (PATH)
Web site and email:
www.brightpathwellnesscentre.example
brightpathchiro@mailbox.example

2 versions of the back of the card:
1. text below
2. appointment schedule card

Text on back of card:
Chiropractic Card text on back of the card:
There is more to chiropractic than the relief of headaches and back pain! Our primary focus is the integrity of your nerve system, which controls and regulates every cell and tissue of your body. The moving bones of the spinal column can impair this vital communication link between your brain and body. We help improve the function and structure of your spine, reducing nerve system compromise. The result?
Even non-spinal related health problems can show improvement
without drugs
without surgery
regardless of age
for over a century
naturally

Appointment Card info For Back:
Please integrate design elements from the front of the card into an appointment card format.
M Tu W Th F Sat (and a line for writing on beside each one)

```html
<!DOCTYPE html>
<html lang="en">
<head>
<meta charset="utf-8">
<title>Bright Path Wellness Centre – Business Card</title>
<link href="https://fonts.googleapis.com/css2?family=Montserrat:wght@400;500;600;700&display=swap" rel="stylesheet">
<style>
  :root {
    --bg: #2a2a2c;
    --card-dark: #1c1c1c;
    --card-light: #ffffff;
    --green: #8cc152;
    --green-soft: #b9dc8e;
    --ink: #2b2b2b;
    --ink-soft: #555555;
    --on-dark: #e8e8e8;
  }
  * { box-sizing: border-box; margin: 0; padding: 0; }
  html, body { width: 1200px; height: 900px; overflow: hidden; }
  body {
    background: var(--bg);
    font-family: "Montserrat", sans-serif;
    position: relative;
  }
  .card {
    position: absolute;
    width: 600px;
    height: 345px;
    border-radius: 20px;
    overflow: hidden;
  }

  /* Appointment back */
  .card-back {
    left: 50px; top: 60px;
    background: var(--card-light);
    color: var(--ink);
    padding: 28px 32px;
  }
  .appt-row {
    display: flex;
    align-items: flex-end;
    gap: 8px;
    font-size: 12px;
    font-weight: 500;
    margin-bottom: 13px;
  }
  .appt-label { white-space: nowrap; }
  .appt-line { flex: 1; border-bottom: 1px solid var(--ink-soft); height: 12px; }
  .appt-days { white-space: nowrap; font-size: 10.5px; color: var(--ink-soft); }
  .about {
    margin-top: 6px;
    font-size: 10.5px;
    line-height: 1.35;
    color: var(--ink);
  }
  .benefits { list-style: none; font-size: 10.5px; line-height: 1.3; margin-top: 1px; }
  .signature { margin-top: 10px; }
  .signature-name {
    color: var(--green);
    font-weight: 700;
    font-size: 19px;
    letter-spacing: 0.5px;
    text-transform: uppercase;
  }
  .signature-role { font-size: 12px; color: var(--ink); }

  /* Practitioner front */
  .card-front {
    left: 550px; top: 490px;
    background: var(--card-dark);
    color: var(--on-dark);
    padding: 36px 36px;
  }
  .feature-art {
    position: absolute; right: 0; top: 0;
    width: 290px; height: 250px;
    background: linear-gradient(225deg, var(--green) 0%, var(--green-soft) 38%, rgba(140,193,82,0.35) 70%, rgba(28,28,28,0) 100%);
    border-bottom-left-radius: 100% 100%;
  }
  .brand {
    position: relative;
    display: flex;
    align-items: center;
    gap: 8px;
    font-size: 17px;
    font-weight: 600;
    color: var(--green);
    letter-spacing: 0.3px;
  }
  .brand-dot { width: 12px; height: 12px; border-radius: 50%; background: var(--green); }
  .practitioner { position: relative; margin-top: 26px; }
  .practitioner-name { color: var(--green); font-weight: 700; font-size: 23px; }
  .practitioner-title { font-size: 13.5px; margin-top: 2px; }
  .address { position: relative; margin-top: 20px; font-size: 13.5px; line-height: 1.35; font-style: normal; }
  .contact { position: relative; margin-top: 16px; list-style: none; font-size: 13px; line-height: 1.6; }
  .contact li { display: flex; align-items: center; gap: 9px; }
  .contact svg { width: 13px; height: 13px; flex: none; }
</style>
</head>
<body>

<section class="card card-back" aria-label="Appointment card back">
  <div class="appt-row">
    <span class="appt-label">Name :</span><span class="appt-line"></span>
  </div>
  <div class="appt-row">
    <span class="appt-label">Time :</span><span class="appt-line"></span>
    <span class="appt-days">(M Tu W Th F Sat)</span>
    <span class="appt-label">Date :</span><span class="appt-line"></span>
    <span class="appt-days">(M Tu W Th F Sat)</span>
  </div>
  <p class="about">There is more to chiropractic than the relief of headaches and back pain! Our primary focus is the integrity of your nerve system, which controls and regulates every cell and tissue of your body. The moving bones of the spinal column can impair this vital communication link between your brain and body. We help improve the function and structure of your spine, reducing nerve system compromise. The result?</p>
  <ul class="benefits">
    <li>Even non-spinal related health problems can show improvement</li>
    <li>without drugs</li>
    <li>without surgery</li>
    <li>regardless of age</li>
    <li>for over a century</li>
    <li>naturally</li>
  </ul>
  <div class="signature">
    <div class="signature-name">Lena Worsick</div>
    <div class="signature-role">Cardiologist</div>
  </div>
</section>

<section class="card card-front" aria-label="Business card front">
  <div class="feature-art" role="img" aria-label="Large green and white brand artwork area"></div>
  <div class="brand"><span class="brand-dot"></span>Bright Path Wellness Centre</div>
  <div class="practitioner">
    <div class="practitioner-name">Dr. Marten Quovel B.Sc</div>
    <div class="practitioner-title">D.C. Chiropractor</div>
  </div>
  <address class="address">
    218 Farrow Gate<br>Etobicoke ON.<br>K2J 6P4
  </address>
  <ul class="contact">
    <li><svg viewBox="0 0 12 12"><circle cx="6" cy="6" r="6" fill="#8cc152"/><path d="M4 3.2l1 1.4-.6.7c.4.8 1 1.4 1.8 1.8l.7-.6 1.4 1-.6 1.2C5.6 8.6 3.4 6.4 3 4z" fill="#1c1c1c"/></svg>416-872-0196 (PATH)</li>
    <li><svg viewBox="0 0 12 12"><rect x="1" y="2.5" width="10" height="7" rx="1" fill="#8cc152"/><path d="M1.5 3l4.5 3.5L10.5 3" stroke="#1c1c1c" fill="none"/></svg>brightpathchiro@mailbox.example</li>
    <li><svg viewBox="0 0 12 12"><circle cx="6" cy="6" r="5.5" fill="#8cc152"/><path d="M.5 6h11M6 .5c-2.5 3-2.5 8 0 11M6 .5c2.5 3 2.5 8 0 11" stroke="#1c1c1c" stroke-width=".8" fill="none"/></svg>www.brightpathwellnesscentre.example</li>
  </ul>
</section>

</body>
</html>
```